Corporate Business Card

Very professional, Modern, Not to busy, include phone address email, website
(555) 317-4860, 18716 52nd Avenue S, Kent, WA 98417, marcus@bralvintrust.example, vendrikworks.example

Target Market(s)

Manufacturing

Industry/Entity Type

Aero, machining, manufacturing, Off road racing

Contact Information for Business Card

Phone, address email, website

```html
<!DOCTYPE html>
<html lang="en">
<head>
<meta charset="utf-8">
<title>Vendrik Works – Business Card</title>
<link rel="stylesheet" href="https://fonts.googleapis.com/css2?family=Open+Sans:wght@400;700&display=swap">
<style>
  :root {
    --backdrop: #8a8a88;
    --navy: #22366b;
    --red: #d3222a;
    --white: #ffffff;
    --ink: #4a4a4a;
    --rule: #7c86a6;
  }
  * { box-sizing: border-box; margin: 0; padding: 0; }
  html, body { width: 1200px; height: 801px; overflow: hidden; }
  body {
    background: var(--backdrop);
    font-family: "Open Sans", sans-serif;
    position: relative;
  }
  .card {
    position: absolute;
    top: 252px;
    width: 520px;
    height: 297px;
    overflow: hidden;
    box-shadow: 0 10px 24px rgba(0,0,0,.25);
    border-bottom: 2px solid var(--red);
  }
  .card-front { left: 60px; background: var(--white); }
  .card-back  { left: 620px; background: var(--navy); }

  .swoosh { position: absolute; inset: 0; width: 520px; height: 297px; }

  .brand {
    position: absolute;
    display: flex;
    align-items: center;
    gap: 10px;
    font-weight: 700;
    white-space: nowrap;
  }
  .brand-mark { display: block; background: var(--red); }
  .brand-rule { position: absolute; height: 2px; }

  .card-front .brand { left: 30px; top: 110px; font-size: 26px; color: var(--navy); }
  .card-front .brand-mark { width: 12px; height: 12px; }
  .card-front .brand-rule { left: 56px; top: 160px; width: 150px; background: var(--navy); }

  .divider {
    position: absolute;
    left: 250px; top: 66px;
    width: 1px; height: 112px;
    background: var(--rule);
  }
  .contact {
    position: absolute;
    left: 266px; top: 70px;
    list-style: none;
    font-size: 12.5px;
    line-height: 20px;
    color: var(--ink);
  }
  .contact li { display: flex; align-items: center; gap: 7px; white-space: nowrap; }
  .contact .icon { width: 11px; height: 11px; flex: none; fill: var(--red); }

  .card-back .brand { left: 70px; top: 112px; font-size: 48px; color: var(--white); }
  .card-back .brand-mark { width: 18px; height: 18px; }
  .card-back .brand-rule { left: 60px; top: 190px; width: 250px; background: var(--white); }
</style>
</head>
<body>

  <section class="card card-front">
    <svg class="swoosh" viewBox="0 0 520 297" aria-hidden="true">
      <path fill="var(--red)" d="M60,297 C290,284 450,244 520,158 L520,170 C455,254 300,290 110,297 Z"/>
      <path fill="var(--navy)" d="M125,297 C320,287 462,250 520,176 L520,297 Z"/>
    </svg>

    <div class="brand"><span class="brand-mark"></span>Vendrik Works</div>
    <div class="brand-rule"></div>

    <div class="divider"></div>
    <ul class="contact">
      <li>18716 52nd Avenue S</li>
      <li>Kent, WA 98417</li>
      <li>
        <svg class="icon" viewBox="0 0 12 12" aria-hidden="true"><path d="M2.5 0.8 L4.6 3 L3.6 4.3 C4.3 5.9 6 7.7 7.7 8.4 L9 7.4 L11.2 9.5 L9.8 11.2 C5 10.6 1.4 7 0.8 2.2 Z"/></svg>
        (555) 317-4860
      </li>
      <li>
        <svg class="icon" viewBox="0 0 12 12" aria-hidden="true"><path d="M0.5 2.5 H11.5 V9.5 H0.5 Z M1.5 3.3 L6 6.6 L10.5 3.3" stroke="var(--white)" stroke-width="0.9"/></svg>
        marcus@bralvintrust.example
      </li>
      <li>
        <svg class="icon" viewBox="0 0 12 12" aria-hidden="true"><circle cx="6" cy="6" r="5.5"/><path d="M0.8 6 H11.2 M6 0.5 C3.4 3.5 3.4 8.5 6 11.5 M6 0.5 C8.6 3.5 8.6 8.5 6 11.5" stroke="var(--white)" stroke-width="0.8" fill="none"/></svg>
        vendrikworks.example
      </li>
    </ul>
  </section>

  <section class="card card-back">
    <div class="brand"><span class="brand-mark"></span>Vendrik Works</div>
    <div class="brand-rule"></div>
  </section>

</body>
</html>
```